VELDRANE KESTO CHANDLERS SELL SHEETS

Create a group of Sell Sheets that can be used in client meetings and willbe incorporated into web site pages in the future. We wish to highlight our Mission Statement / Company Bio / Services and Products offered. This piece may be 8 to 12 pages. In the near future this will grow to include an on-line Catalog with 300 to 500 pages of product offerings.

It will not list individual products and prices but rather will serve as a New Business introduction using brief descriptive text and a lot of industry photos. At this time we do have a Logo and Tag Line which will be used.

The image we need to portray is High End Quality Sales, Service, Professional Industry Experience and Reliability. My personal experience includes 27 years as a ship´s Captain working all over the world.

We are a start-up Ship´s Chandler service, located in Macae, Brasil. We will sell products and inspection services to the Offshore Petroleum Industry which includes vessels and platforms. These products will include the simple monthly supply replenishment (like paper towels / laundry soap / drinking water) to the more technical, like Pop Off Valves (sales & inspection certifications), Transfer Hoses, Sales Service and Certifications, OEM Filters for Engines& Generators, Anchor Harware, Nautical Bulbs & Light Fixtures Safety Gear and hundreds of other items.

We will have a group of EMERGENCY GEAR on-hand in our warehouse, to supply in cases like a lost anchor for example. We willoffer a Guaranteed 30 hour delivery anywhere in Brasil. These vessels work at a rate of up to $50K per day and cannot afford what is called`Down Time` or time off the clock.

All text will be supplied in both English and Portuguese. I prefer that each block of text will show both languages with a distinctive color or typeface for each. Please present your ideas on how to deal with the two languages.

Sorry for any mis-spellings but today I am forced to work on a Portuguese keyboard.

Target Market(s)

Ship´s Captains, Purchasing Managers, Company Directors, Engineers

Industry/Entity Type

Business

Requirements
Must have
• I am open to a Professional, High End look. I would like to incorporate photos and ``historical`` illustrations to tella story, which I will supply.

I have attached our new Company Logo which has the tag line....``TO STAY THE COURSE´´. We would like to repeat the logo and tag line whenever possible without being too obnoxious.

```html
<!DOCTYPE html>
<html lang="en">
<head>
<meta charset="utf-8">
<title>Veldrane Kesto Chandlers – Sell Sheet</title>
<link rel="stylesheet" href="https://fonts.googleapis.com/css2?family=Open+Sans:wght@700&family=Mulish:wght@700;800&family=Carlito:ital,wght@0,400;0,700;1,400;1,700&display=swap">
<style>
  :root {
    --header-taupe: #968b87;
    --ink: #111111;
    --ink-muted: #7a7a7a;
    --navy: #3f5a8c;
    --orange: #e3996b;
    --taupe: #958985;
    --gold: #fbc43a;
    --white: #ffffff;
    --paper: #ffffff;
  }
  * { box-sizing: border-box; margin: 0; padding: 0; }
  html, body { width: 927px; height: 1200px; overflow: hidden; background: var(--paper); }
  body { position: relative; font-family: "Carlito", "Calibri", sans-serif; color: var(--ink); }

  .masthead {
    position: absolute; left: 0; top: 0; width: 927px; height: 157px;
    background: var(--header-taupe);
    box-shadow: 0 6px 8px rgba(0,0,0,.35);
    display: flex; align-items: center; justify-content: center;
  }
  .masthead h1 {
    font-family: "Open Sans", sans-serif; font-weight: 700;
    color: var(--white); font-size: 47px; letter-spacing: 1px; margin-top: -8px;
  }

  .intro { position: absolute; top: 196px; width: 270px; }
  .intro h2 { font-style: italic; font-weight: 700; color: var(--navy); font-size: 21px; margin-bottom: 14px; }
  .intro p { font-size: 16px; line-height: 22.2px; }
  .intro--en { left: 46px; }
  .intro--pt { left: 330px; }
  .intro--pt p { color: var(--ink-muted); }

  .hero-wheel {
    position: absolute; left: 646px; top: 282px; width: 250px; height: 200px;
    border-radius: 50%;
    background: radial-gradient(circle at 45% 40%, #d8b96a 0%, #a8853a 45%, #6e5423 75%, rgba(110,84,35,0) 100%);
  }

  .service {
    position: absolute; top: 597px; width: 260px; height: 164px;
    padding: 12px 10px 0 10px;
    box-shadow: 4px 5px 6px rgba(0,0,0,.45);
    color: var(--white);
  }
  .service h3 { font-weight: 700; font-size: 22px; line-height: 28px; }
  .service p { font-style: italic; color: var(--ink); font-size: 13.5px; line-height: 18px; margin-top: 2px; }
  .service--supply { left: 46px; background: var(--orange); }
  .service--technical { left: 336px; background: var(--taupe); }
  .service--emergency { left: 625px; background: var(--gold); }

  .call-to-action { position: absolute; left: 0; top: 812px; width: 927px; text-align: center; color: var(--navy); font-family: "Mulish", sans-serif; }
  .call-to-action h2 { font-weight: 800; font-size: 35px; letter-spacing: .5px; }
  .call-to-action p { font-weight: 700; font-size: 22.5px; margin-top: 4px; }

  .closing { position: absolute; top: 934px; width: 240px; font-style: italic; font-size: 14.6px; line-height: 20px; }
  .closing--en { left: 54px; }
  .closing--pt { left: 325px; color: var(--ink-muted); }

  .brand-block {
    position: absolute; left: 602px; top: 944px; width: 294px; height: 210px;
    background: linear-gradient(#f6f5f1, #eceae4);
    display: flex; flex-direction: column; align-items: center; justify-content: center; gap: 12px;
  }
  .brand-block .brand-dot { width: 46px; height: 46px; border-radius: 50%; background: var(--gold); }
  .brand-block .brand-name { font-weight: 700; font-size: 19px; color: var(--navy); letter-spacing: .5px; }

  .footer { position: absolute; left: 46px; top: 1119px; width: 500px; text-align: center; font-style: italic; font-size: 16.5px; line-height: 22px; }
</style>
</head>
<body>
  <header class="masthead"><h1>VELDRANE KESTO CHANDLERS</h1></header>

  <section class="intro intro--en" lang="en">
    <h2>“To Stay the Course”</h2>
    <p>High-end sales and service, extensive industry experience, reliability.From Macae, Brasil, we offer products and inspection services to the Offshore Petroleum Industry. Large or small, routine or emergency, we have you covered. We understand the seriousness of surprise downtime, and work to fulfil the unexpected needs of our clients, supplying lost or damaged equipment within thirty hours, guaranteed.</p>
  </section>

  <section class="intro intro--pt" lang="pt">
    <h2>“Mantenham o Curso”</h2>
    <p>Alta qualidade de vendas e serviços, ampla experiência da indústria, confiabilidade. De Macaé, Brasil, oferecemos produtos e serviços de inspeção para a Indústria de Petróleo Offshore. Grande ou pequena rotina, ou de emergência, temos que cobertas. Entendemos a gravidade da paralisação surpresa, e trabalhar para satisfazer as ne­cessidades inesperadas de nossos clientes, fornecendo perdido ou danificado equipamento dentro 30 horas, garantido.</p>
  </section>

  <div class="hero-wheel" role="img" aria-label="Photograph of a brass ship's steering wheel"></div>

  <article class="service service--supply">
    <h3>Monthly Supply &amp; Replenishment –</h3>
    <p>Keep on top of your day to-day needs</p>
  </article>
  <article class="service service--technical">
    <h3>Technical &amp; Specialty Equipment</h3>
    <p>A wide array of nautical hardware</p>
  </article>
  <article class="service service--emergency">
    <h3>Emergency Gear – Guaranteed Delivery</h3>
    <p>Within thirty hours, replacements for lost or damaged equipment</p>
  </article>

  <section class="call-to-action">
    <h2>TO STAY THE COURSE.</h2>
    <p>Get in touch today to see how we can support your operations.</p>
  </section>

  <p class="closing closing--en">Lorem Ipsum is simply dummy text of the printing and typesetting industry. Lorem Ipsum has been the industry’s standard dummy text ever since the 1500s, when an unknown printer took a galley of type and scrambled it to make...</p>
  <p class="closing closing--pt" lang="pt">O Lorem Ipsum é um texto modelo da indústria tipográfica e de im­pressão. O Lorem Ipsum tem vindo a ser o texto padrão usado por estas indústrias desde o ano de 1500, quando uma misturou os caracteres de um texto...</p>

  <div class="brand-block">
    <span class="brand-dot"></span>
    <span class="brand-name">VELDRANE KESTO CHANDLERS</span>
  </div>

  <footer class="footer">
    contact information • contact information • contact info<br>
    legal info, boilerplate footer material et cetera
  </footer>
</body>
</html>
```